依頼詳細
現行のホームページがかなり以前のものになりますので、今回の
リニューアルを機に、デザインの刷新を希望しております。

かしこまりすぎず、先鋭的で、現代的なデザインを希望しております。
動線が明確で、ユーザーが迷子にならないようなものを希望しております。
あくまでイメージとしての簡潔なワイヤーフレームを添付しておりますが、
ランサー様の自由なご発想によるデザインを期待しております。

デザインの参考にして頂きたいサイトを共有いたしますのでご確認ください。

https://www.minatoseiki.jp/
上記サイトのようなお知らせの表示を希望します。

https://haruden-na.com/
グループ支社となります。MVは動画も検討しております。

https://haruden.co.kr/

https://www.valmerco.com/
色味・構成が希望に近いです。

https://www.tqr-inc.co.jp/
コンテンツ配置が希望と似ております。

※その他詳細内容はTOPデザイン要望書と下記添付ファイルをご確認ください。
パスワードは補足説明内に記載しております。
https://filevaultex.com/download/a7e21f90bd3c44d8a2c6f05e18b7d2c94e61f03a
青系、水色系
• イラストレーター形式 (.ai)
• フォトショップ形式 (.psd)
■写真・データ(添付ファイル内) パスワード:qmd384527
Pixmora Stock [ https://stock.pixmora-example.com/jp/ ] で定期契約をしています。
また定期契約のものは弊社の負担となり、ランサー様に負担はありません。
カンプ画像を入れてください。その際、通常アセットで購入できる画像でお願いいたします。

■サイトマップ・ワイヤーフレーム(添付ファイル内)
デザイナー様で一案感じられる箇所がございましたら、ご提案いただければ幸いです。

■文章について
ワイヤーフレーム内に記載されているテキストを使用してください。
可能な限り「ダミーテキスト」を繰り返した表記は避けていただけますと幸いです。

■フォントについて
・WEB上で使用可能な無料のフォントで作成お願い致します。
・OSに紐づくフォントの使用は控えていただければと思います 。(ヒラギノなど)

■サイズについて
TOPデザイン自体の画像サイズは、横幅1300pxで提案をお願いできればと思います。(縦幅の制限はございません)

※通常業務へ支障をきたす為、当企業へのお問い合わせはお控え下さい。
皆様ご提案くださりありがとうございます。
様々なパターンで検討させていただきたいので、期限を延長させていただきます。
ワイヤーフレーム通りではなく、自由なご発想でのご提案もお待ちしております。
皆様ご提案くださりありがとうございます。
様々なバリエーションで検討させていただきたい為、
期限いっぱいまで延長とさせていただきます。

```html
<!DOCTYPE html>
<html lang="ja">
<head>
<meta charset="utf-8">
<title>HARUDEN | 油圧に生きる</title>
<link href="https://fonts.googleapis.com/css2?family=Noto+Sans+JP:wght@400;500;700;900&family=Oswald:wght@500;700&display=swap" rel="stylesheet">
<style>
:root{
  --navy:#14305e;
  --navy-deep:#0e2348;
  --blue:#1f5fbf;
  --blue-bright:#2d78d8;
  --sky:#dbe7f5;
  --pale:#eef2f7;
  --ink:#222a36;
  --muted:#6b7585;
  --line:#d6dde7;
  --orange:#f09a1a;
  --red:#d8373a;
  --white:#ffffff;
}
*{box-sizing:border-box;margin:0;padding:0}
html,body{width:1200px;height:3904px;overflow:hidden}
body{font-family:"Noto Sans JP",sans-serif;color:var(--ink);background:var(--white);position:relative}
a{color:inherit;text-decoration:none}
.sec{position:absolute;left:0;width:1200px}

/* header */
.site-header{top:0;height:64px;background:var(--white);border-bottom:1px solid var(--line)}
.brand{position:absolute;left:28px;top:20px;display:flex;align-items:center;gap:8px}
.brand-mark{width:12px;height:12px;background:var(--blue-bright)}
.brand-name{font-size:20px;font-weight:700;color:var(--navy);letter-spacing:.06em;line-height:1}
.util{position:absolute;right:28px;top:6px;display:flex;gap:14px;font-size:10px;color:var(--muted)}
.global-nav{position:absolute;left:270px;top:22px;display:flex;height:42px}
.global-nav a{width:104px;background:var(--navy);color:var(--white);font-size:12px;font-weight:500;display:flex;align-items:center;justify-content:center;border-right:1px solid #2a4776}
.global-nav a.is-active{background:var(--blue-bright)}
.global-nav a.contact{background:var(--navy-deep)}

/* hero */
.hero{top:64px;height:576px}
.hero-photo{position:absolute;inset:0;background:linear-gradient(120deg,#9fb6cf 0%,#d4e0ec 30%,#5d7898 55%,#1f3a63 80%,#0d2245 100%)}
.hero-sub{position:absolute;left:270px;top:0;height:30px;width:660px;background:rgba(255,255,255,.92);display:flex;gap:18px;align-items:center;padding-left:14px;font-size:10px;color:var(--navy)}
.hero-sub b{background:var(--blue-bright);color:var(--white);padding:4px 10px;font-weight:500}
.hero-copy{position:absolute;right:96px;top:330px;font-size:52px;font-weight:900;color:var(--white);letter-spacing:.06em}
.hero-copy em{font-style:normal;color:var(--orange)}
.hero-btn{position:absolute;right:96px;top:420px;width:210px;height:42px;background:var(--white);color:var(--navy);font-size:13px;display:flex;align-items:center;justify-content:space-between;padding:0 18px}
.dots{position:absolute;left:0;right:0;display:flex;justify-content:center;gap:8px}
.dots i{width:8px;height:8px;border-radius:50%;background:rgba(255,255,255,.6)}
.dots i.on{background:var(--white)}
.hero .dots{bottom:18px}

/* section headings */
.sec-title{text-align:center}
.sec-title h2{font-family:"Oswald",sans-serif;font-weight:700;font-size:46px;color:var(--navy);letter-spacing:.04em;line-height:1}
.sec-title p{font-size:11px;color:var(--muted);margin-top:6px}

/* news */
.news{top:640px;height:650px;background:var(--white)}
.news .sec-title{margin-top:46px}
.news-tabs{position:absolute;left:100px;top:166px;display:flex;width:840px}
.news-tabs a{flex:1;height:40px;border:1px solid var(--line);display:flex;align-items:center;justify-content:center;font-size:12px;color:var(--navy)}
.news-tabs a.is-active{background:var(--blue-bright);color:var(--white);border-color:var(--blue-bright)}
.news-more{position:absolute;right:100px;top:166px;width:130px;height:40px;border:1px solid var(--blue-bright);color:var(--blue-bright);font-size:11px;display:flex;align-items:center;justify-content:center;gap:8px}
.news-list{position:absolute;left:100px;top:222px;width:1000px;list-style:none;border-top:1px solid var(--line)}
.news-list li{height:74px;border-bottom:1px solid var(--line);display:flex;align-items:center;gap:22px;font-size:12px;padding-left:10px}
.news-list time{width:80px;color:var(--muted);font-size:11px}
.tag{width:84px;height:22px;display:flex;align-items:center;justify-content:center;font-size:10px;color:var(--white);background:var(--orange)}
.tag.blue{background:var(--blue-bright)}

/* about */
.about{top:1290px;height:820px}
.about .sec-title{margin-top:34px}
.about-lead{text-align:center;font-size:12px;line-height:2;color:var(--ink);margin-top:28px}
.about-grid{position:absolute;left:100px;top:210px;width:1000px;display:grid;grid-template-columns:1fr 1fr;gap:20px}
.card{height:280px;position:relative;overflow:hidden}
.card-photo{position:absolute;inset:0}
.card-label{position:absolute;left:0;right:0;bottom:24px;text-align:center;color:var(--white);font-size:20px;font-weight:700;letter-spacing:.1em}
.corp{background:var(--navy);padding:26px 34px}
.corp h3{color:var(--white);font-size:20px;text-align:center;margin-bottom:18px;letter-spacing:.1em}
.corp-links{display:grid;grid-template-columns:1fr 1fr;gap:10px}
.corp-links a{height:36px;background:var(--white);color:var(--navy);font-size:11px;display:flex;align-items:center;justify-content:space-between;padding:0 12px}
.corp-links a.lead{background:var(--orange);color:var(--white)}

/* product */
.product{top:2110px;height:790px;background:linear-gradient(#e4e9f0,#f6f8fb 180px,var(--white) 300px)}
.product .sec-title{margin-top:62px}
.prod-main{position:absolute;left:100px;top:250px;width:1000px;display:grid;grid-template-columns:repeat(4,1fr);gap:16px}
.prod-card{height:160px;position:relative}
.prod-card span{position:absolute;left:0;bottom:0;background:var(--white);color:var(--navy);font-size:12px;font-weight:700;padding:7px 14px}
.prod-sub{position:absolute;left:100px;top:440px;width:1000px;display:grid;grid-template-columns:repeat(5,1fr);gap:14px}
.prod-item{height:190px;background:var(--white);position:relative}
.prod-item .ph{position:absolute;left:18px;right:18px;top:16px;height:120px}
.prod-item span{position:absolute;left:50%;transform:translateX(-50%);bottom:16px;background:var(--navy);color:var(--white);font-size:10px;padding:5px 14px;white-space:nowrap}
.product .dots{top:700px}
.product .dots i{background:#b8c4d4}
.product .dots i.on{background:var(--navy)}

/* banners */
.banners{top:2900px;height:520px;background:linear-gradient(#8a8f96,#c9cdd2 40%,#e9ebee)}
.ban-big{position:absolute;top:64px;width:480px;height:130px;background:linear-gradient(110deg,#1b1f26,#3a4350);display:flex;flex-direction:column;justify-content:center;padding-left:40px;color:var(--white)}
.ban-big b{font-size:24px;letter-spacing:.1em}
.ban-big small{font-size:10px;opacity:.8;margin-top:4px}
.ban-sm{position:absolute;top:300px;width:240px;height:110px;background:linear-gradient(110deg,#16345f,#2c5a93);color:var(--white);display:flex;align-items:center;justify-content:center;text-align:center;font-size:15px;font-weight:700;line-height:1.5;padding:0 10px}
.ban-sm.gray{background:linear-gradient(110deg,#e9edf2,#c7d2de);color:var(--navy)}
.cta{position:absolute;left:880px;width:220px;height:50px;color:var(--white);font-size:14px;font-weight:700;display:flex;align-items:center;gap:12px;padding-left:24px}
.cta.red{top:300px;background:var(--red)}
.cta.blue{top:360px;background:var(--blue)}

/* footer */
.site-footer{top:3420px;height:484px;background:var(--navy-deep);color:var(--white)}
.foot-brand{position:absolute;left:0;right:0;top:44px;display:flex;justify-content:center;align-items:center;gap:8px}
.foot-brand .brand-mark{background:var(--white)}
.foot-brand .brand-name{color:var(--white)}
.foot-btns{position:absolute;right:100px;top:34px;display:flex;gap:10px}
.foot-btns a{border:1px solid #5d759b;font-size:10px;padding:6px 14px}
.foot-cols{position:absolute;left:100px;top:124px;width:1000px;display:grid;grid-template-columns:repeat(5,1fr);gap:20px;border-top:1px solid #2f4670;padding-top:26px}
.foot-cols h4{font-size:13px;margin-bottom:14px}
.foot-cols ul{list-style:none}
.foot-cols li{font-size:10px;color:#b9c5d8;margin-bottom:9px}
.foot-cols li::before{content:"› ";color:var(--blue-bright)}
.copyright{position:absolute;left:0;right:0;bottom:0;height:40px;background:#09193a;font-size:10px;color:#9aa9c0;display:flex;align-items:center;justify-content:center;gap:30px}
</style>
</head>
<body>

<header class="sec site-header">
  <div class="brand"><span class="brand-mark"></span><span class="brand-name">HARUDEN</span></div>
  <div class="util"><span>ログイン</span><span>検索</span><span>JP / EN</span></div>
  <nav class="global-nav">
    <a class="is-active" href="#">企業情報</a><a href="#">IR情報</a><a href="#">製品情報</a><a href="#">販売ネットワーク</a><a href="#">油圧セミナー</a><a href="#">採用情報</a><a class="contact" href="#">お問い合わせ</a>
  </nav>
</header>

<section class="sec hero">
  <div class="hero-photo" role="img" aria-label="工場内で稼働する産業機械のラインの写真"></div>
  <div class="hero-sub"><b>企業情報</b><span>› 会社概要</span><span>› 企業理念</span><span>› 沿革</span></div>
  <p class="hero-copy"><em>油圧</em>に生きる</p>
  <a class="hero-btn" href="#">詳細情報 <span>→</span></a>
  <div class="dots"><i class="on"></i><i></i><i></i><i></i><i></i><i></i><i></i><i></i></div>
</section>

<section class="sec news">
  <div class="sec-title"><h2>NEWS</h2><p>最新情報</p></div>
  <div class="news-tabs"><a class="is-active" href="#">お知らせ</a><a href="#">製品ニュース</a><a href="#">IRニュース</a></div>
  <a class="news-more" href="#">お知らせ一覧 <span>→</span></a>
  <ul class="news-list">
    <li><time>2022.04.01</time><span class="tag blue">お知らせ</span><span>組織変更および人事異動に関するお知らせ（新体制のご案内）</span></li>
    <li><time>2022.03.25</time><span class="tag">製品ニュース</span><span>新型可変ポンプシリーズの販売開始について</span></li>
    <li><time>2022.03.10</time><span class="tag">製品ニュース</span><span>総合カタログ最新版の公開および資料請求受付のご案内</span></li>
    <li><time>2022.02.28</time><span class="tag">製品ニュース</span><span>展示会出展のお知らせ</span></li>
    <li><time>2022.02.15</time><span class="tag blue">IRニュース</span><span>決算説明資料を掲載しました</span></li>
  </ul>
</section>

<section class="sec about">
  <div class="sec-title"><h2>ABOUT US</h2><p>私たちについて</p></div>
  <p class="about-lead">創業以来、油圧機器の専門メーカーとして技術を磨き、世界の産業を支えてきました。<br>製品・販売網・サービスを通じて、持続可能なものづくりに貢献してまいります。</p>
  <div class="about-grid">
    <div class="card corp">
      <h3>企業情報</h3>
      <div class="corp-links">
        <a class="lead" href="#">トップメッセージ <span>›</span></a><a href="#">会社概要 <span>›</span></a>
        <a href="#">企業理念 <span>›</span></a><a href="#">工場・拠点一覧 <span>›</span></a>
        <a href="#">沿革 <span>›</span></a><a href="#">グループ企業 <span>›</span></a>
        <a href="#">品質・環境への取組み <span>›</span></a><a href="#">社会貢献活動 <span>›</span></a>
      </div>
    </div>
    <div class="card"><div class="card-photo" role="img" aria-label="グラフや資料が並ぶデスクの写真" style="background:linear-gradient(135deg,#e8eef5,#9fb9d6 60%,#5c80ad)"></div><p class="card-label">IR情報</p></div>
    <div class="card"><div class="card-photo" role="img" aria-label="スーツ姿で握手を交わすビジネスシーンの写真" style="background:linear-gradient(135deg,#d9dee4,#8a96a4 55%,#3f4a58)"></div><p class="card-label">採用情報</p></div>
    <div class="card"><div class="card-photo" role="img" aria-label="高層ビルが並ぶ都市の空撮写真" style="background:linear-gradient(180deg,#bcd4ec,#7d9cbf 55%,#4b6587)"></div><p class="card-label">販売ネットワーク</p></div>
  </div>
</section>

<section class="sec product">
  <div class="sec-title"><h2>PRODUCT</h2><p>製品情報</p></div>
  <div class="prod-main">
    <div class="prod-card" role="img" aria-label="油圧ポンプ製品の写真" style="background:linear-gradient(135deg,#cfd6de,#6f7c8b)"><span>油圧機器</span></div>
    <div class="prod-card" role="img" aria-label="リニアサーボ弁製品の写真" style="background:linear-gradient(135deg,#e5f0fb,#6aa0d8)"><span>油圧製品機器</span></div>
    <div class="prod-card" role="img" aria-label="環境機器のユニット写真" style="background:linear-gradient(135deg,#dfe8f1,#8ea9c4)"><span>環境機器</span></div>
    <div class="prod-card" role="img" aria-label="製鉄工場の高温の現場写真" style="background:linear-gradient(135deg,#f3a35a,#7a2f1a)"><span>油圧セミナー</span></div>
  </div>
  <div class="prod-sub">
    <div class="prod-item"><div class="ph" role="img" aria-label="ピストンポンプの製品写真" style="background:linear-gradient(#eef1f4,#7d8896)"></div><span>ピストンポンプ</span></div>
    <div class="prod-item"><div class="ph" role="img" aria-label="ベーンポンプの製品写真" style="background:linear-gradient(#eef1f4,#5d6977)"></div><span>ベーンポンプ</span></div>
    <div class="prod-item"><div class="ph" role="img" aria-label="油圧ユニットの製品写真" style="background:linear-gradient(#eef3f9,#5e86b8)"></div><span>油圧ユニット</span></div>
    <div class="prod-item"><div class="ph" role="img" aria-label="電磁弁の製品写真" style="background:linear-gradient(#eef3f9,#3f6ea8)"></div><span>電磁切換弁</span></div>
    <div class="prod-item"><div class="ph" role="img" aria-label="サーボ弁の製品写真" style="background:linear-gradient(#eef3f9,#2f5a92)"></div><span>サーボ弁</span></div>
  </div>
  <div class="dots"><i class="on"></i><i></i><i></i><i></i><i></i></div>
</section>

<section class="sec banners">
  <a class="ban-big" href="#" style="left:100px"><b>採用情報</b><small>未来を一緒に創る仲間を募集</small></a>
  <a class="ban-big" href="#" style="left:620px"><b>展示会</b><small>出展情報・イベントのご案内</small></a>
  <a class="ban-sm" href="#" style="left:100px">ハルデンのイチオシ</a>
  <a class="ban-sm gray" href="#" style="left:360px">総合カタログ&amp;<br>油圧製品CADデータ</a>
  <a class="ban-sm" href="#" style="left:620px">ハルデン工業の<br>社会貢献活動</a>
  <a class="cta red" href="#"><svg width="18" height="18" viewBox="0 0 24 24" fill="none" stroke="#fff" stroke-width="2"><rect x="3" y="5" width="18" height="14"/><path d="M3 6l9 7 9-7"/></svg>お問い合わせ</a>
  <a class="cta blue" href="#"><svg width="18" height="18" viewBox="0 0 24 24" fill="none" stroke="#fff" stroke-width="2"><circle cx="12" cy="8" r="4"/><path d="M4 21c0-4 4-6 8-6s8 2 8 6"/></svg>メンバーログイン</a>
</section>

<footer class="sec site-footer">
  <div class="foot-brand"><span class="brand-mark"></span><span class="brand-name">HARUDEN</span></div>
  <div class="foot-btns"><a href="#">メンバーログイン</a><a href="#">お問い合わせ</a></div>
  <div class="foot-cols">
    <div><h4>企業情報</h4><ul><li>トップメッセージ</li><li>会社概要</li><li>企業理念</li><li>沿革</li><li>拠点一覧</li><li>グループ企業</li></ul></div>
    <div><h4>IR情報</h4><ul><li>IRニュース</li><li>決算情報</li><li>株式情報</li><li>IRカレンダー</li></ul></div>
    <div><h4>製品情報</h4><ul><li>油圧機器</li><li>環境機器</li><li>総合カタログ</li><li>CADデータ</li></ul></div>
    <div><h4>販売ネットワーク</h4><ul><li>国内拠点</li><li>海外拠点</li><li>代理店一覧</li></ul></div>
    <div><h4>油圧セミナー</h4><ul><li>セミナー概要</li><li>開催日程</li><li>お申し込み</li></ul></div>
  </div>
  <div class="copyright"><span>2022 © Copyright HARUDEN KOGYO CO.,LTD.</span><span>個人情報保護方針</span></div>
</footer>

</body>
</html>
```